Business Card

I need a business card that is fresh, styling and reflects my heart centered healing business while still maintaining full professionalism as I have an my evidence-based practice. I am a Naturopath and a Shiatsu Massage Therapist.
Below are my existing logo (file 1) and an inspiration image (file 2) that reflects the colours and style I would like to express to my card (blues greens). I especially like that tree wallpaper.

Information for the card:
Tessa Gorrinde
BHSc. (Nat) m.QRPC
Naturopath
Herbalist
Nutritionist
Shiatsu Therapist
Wellness Counsellor

41 Dovertan St South Fremantle
www.tessagorrinde.com.au
tessa@tessagorrinde.com.au

NOte: I've removed part of the brief, in that I've changed my mind about the back of the card being a '5 treatments and get sixth one free" I'd rather have this on a separate card. So please do not include this in your designs.
Updates

Hi Guys, I've taken the '5 session get the sixth free' part out of the brief. Also, I've added the info to go on the business card into the brief.

Thanks and happy designing
Tes

I've just uploaded a high res better quality version of the hand logo. Thanks Lovlies. 

Target Market(s)

I am targeting western women of ages 25 - 40 in preconception care, sugar addiction therapy, and wellness coaching. I want must card to be vibrant, positive and current.

Industry/Entity Type

Business

Requirements
Must have
• Please include my hand image logo

```html
<!DOCTYPE html>
<html lang="en">
<head>
<meta charset="utf-8">
<title>Tessa Gorrinde — Business Card</title>
<link rel="stylesheet" href="https://fonts.googleapis.com/css2?family=Tinos&display=swap">
<style>
  :root {
    --card-sand: #e0c09e;
    --ink-navy: #2b3d8c;
    --leaf-green: #5e7b5c;
    --leaf-mid: #6f8a68;
  }
  html, body {
    margin: 0;
    padding: 0;
    overflow: hidden;
    background: var(--card-sand);
  }
  .card {
    position: relative;
    width: 703px;
    height: 1200px;
    overflow: hidden;
    background: var(--card-sand);
    color: var(--ink-navy);
    font-family: "Tinos", "Times New Roman", serif;
  }
  .line {
    position: absolute;
    left: 0;
    width: 100%;
    margin: 0;
    text-align: center;
    line-height: 1;
    white-space: pre;
    font-weight: 400;
  }
  .name-first {
    top: 129px;
    font-size: 100px;
    letter-spacing: 0.42em;
    padding-left: 0.42em;
    box-sizing: border-box;
  }
  .name-last {
    top: 249px;
    font-size: 82px;
    letter-spacing: 0.01em;
  }
  .credentials { font-size: 37px; }
  .credentials-1 { top: 466px; }
  .credentials-2 { top: 510px; }
  .credentials-3 { top: 553px; }
  .contact { font-size: 36px; }
  .contact-address { top: 714px; }
  .contact-web { top: 758px; }
  .contact-email { top: 802px; }
  .tree-band {
    position: absolute;
    left: 0;
    bottom: 0;
    width: 703px;
    height: 262px;
    display: block;
  }
</style>
</head>
<body>
  <main class="card">
    <h1 class="line name-first">TESSA</h1>
    <p class="line name-last">GORRINDE</p>

    <p class="line credentials credentials-1">BHSc. (Nat) m.QRPC     Naturopath</p>
    <p class="line credentials credentials-2">Herbalist     Nutritionist</p>
    <p class="line credentials credentials-3">Shiatsu Therapist   Wellness Counsellor</p>

    <p class="line contact contact-address">41 Dovertan St South Fremantle</p>
    <p class="line contact contact-web">www.tessagorrinde.com.au</p>
    <p class="line contact contact-email">tessa@tessagorrinde.com.au</p>

    <svg class="tree-band" viewBox="0 0 703 262" role="img" aria-label="Illustrated row of green trees and palm fronds along the bottom of the card">
      <defs>
        <linearGradient id="treeFade" x1="0" y1="0" x2="0" y2="1">
          <stop offset="0" stop-color="#e0c09e"/>
          <stop offset="0.14" stop-color="#6f8a68"/>
          <stop offset="1" stop-color="#5e7b5c"/>
        </linearGradient>
      </defs>
      <rect width="703" height="262" fill="url(#treeFade)"/>
    </svg>
  </main>
</body>
</html>
```